Double Sided Business Card Design for Pet Services

My mom and I want to start a business for pets. We want to offer dog walking, pet sitting as well as boarding and grooming at our home. For the front of the business card, we want a logo that will capture all of our services. We want the name to be Bigotes, Inc., which means little paws in Spanish. Perhaps, there could be little paws or just a little paw implemented within the word Bigotes. Or we would want a cat and a dog by the word Bigotes. We have a cat and a dog at home, and we would be really happy if they could be a part of the business card. It does not have to be anything crazy. Just an outline of a cat or a dog would be awesome. Please see uploaded file.
As for the back of the card, we would want little paws all over the card or we would want a collar, leash, grooming scissor, dog/cat bowl, bone, fish, or toy to show all of the services that we provide. Along with either the many paws or many pet objects, we would want to add our information, such as name (Lorenza Mireles), telephone numbers (555) 812-3762, e-mail addresses bigotesinc@correomail.net, etc.
We would also want a catch phrase to go on the back of the card, such as "Where all paws matter!" Or "We strive for happy tails." or "A paw-bulous service is guaranteed!"
As for colors, we would not want that many. We would want perhaps white and blue. We would want soft colors that will stand out and make an impression. The same goes with the text. An elegant text would be nice. Or perhaps a text with bold letters. We are excited to see the results, but we are also excited to see your creative ideas and what you will bring to the table.

Target Market(s)

Pet Owners

Contact Information for Business Card

For the front of the business card, we want a logo that will capture all of our services. We want the name to be Bigotes, Inc., which means little paws in Spanish. Perhaps, there could be little paws or just a little paw implemented within the word Bigotes. Or we would want a cat and a dog by the word Bigotes. We have a cat and a dog at home, and we would be really happy if they could be a part of the business card. It does not have to be anything crazy. Just an outline of a cat or a dog would be awesome. Please see uploaded file.
As for the back of the card, we would want little paws all over the card or we would want a collar, leash, grooming scissor, dog/cat bowl, bone, fish, or toy to show all of the services that we provide. Along with either the many paws or many pet objects, we would want to add our information, such as name, telephone numbers, e-mail addresses, etc. We would also want a catch phrase to go on the back of the card, such as "Where all paws matter!" Or "We strive happy tails." or "A paw-bulous service is guaranteed!" Or if there is a way to put the catch phrase in the front of the card. We are open to seeing variety.

Logo Text

Bigotes, Inc

Font styles to use
Serif
Script

Colors
ffffff
33a6d7
145ea8

Requirements
Must have
• My project must be a double sided business card.

```html
<!DOCTYPE html>
<html lang="en">
<head>
<meta charset="utf-8">
<title>Bigotes, Inc – Business Card</title>
<link rel="stylesheet" href="https://fonts.googleapis.com/css2?family=Poiret+One&family=Questrial&family=Sriracha&display=swap">
<style>
  :root {
    --page: #ffffff;
    --card-blue: #1b6fc2;
    --card-blue-deep: #145ea8;
    --silver-light: #f7f7f8;
    --silver-dark: #c9cbce;
    --accent-orange: #f5971f;
    --ink: #1c1c1c;
    --white: #ffffff;
  }
  html, body {
    margin: 0;
    width: 1200px;
    height: 900px;
    overflow: hidden;
    background: var(--page);
  }
  .sheet {
    position: relative;
    width: 1200px;
    height: 900px;
    display: flex;
    align-items: center;
    justify-content: center;
    gap: 40px;
  }
  .card {
    position: relative;
    width: 540px;
    height: 310px;
    border-radius: 18px;
    overflow: hidden;
    box-shadow: 0 10px 24px rgba(0,0,0,0.18);
  }

  /* Brand name */
  .brand {
    display: inline-flex;
    align-items: center;
    gap: 12px;
  }
  .brand__dot {
    flex: none;
    border-radius: 50%;
    background: var(--accent-orange);
  }
  .brand__name {
    font-family: "Questrial", sans-serif;
    font-weight: 400;
    color: var(--ink);
    line-height: 1;
    white-space: nowrap;
  }

  /* Back side */
  .card--back {
    background: linear-gradient(180deg, var(--card-blue) 0%, var(--card-blue-deep) 100%);
    text-align: center;
    color: var(--ink);
  }
  .card--back .brand { margin-top: 44px; }
  .card--back .brand__name { font-size: 40px; }
  .card--back .brand__dot { width: 20px; height: 20px; }
  .contact__name {
    margin: 26px 0 0;
    font-family: "Poiret One", sans-serif;
    font-size: 27px;
    color: var(--accent-orange);
    letter-spacing: 0.5px;
  }
  .contact__phone {
    margin: 14px 0 0;
    font-family: "Questrial", sans-serif;
    font-size: 25px;
  }
  .contact__email {
    margin: 2px 0 0;
    font-family: "Questrial", sans-serif;
    font-size: 16px;
  }
  .tagline {
    position: absolute;
    left: 0; right: 0;
    bottom: 24px;
    margin: 0;
    font-family: "Sriracha", cursive;
    font-size: 21px;
    color: var(--white);
    letter-spacing: 0.5px;
  }

  /* Front side */
  .card--front {
    background: radial-gradient(ellipse at 40% 20%, var(--silver-light) 0%, #e6e7e9 55%, var(--silver-dark) 100%);
  }
  .card__wave {
    position: absolute;
    inset: 0;
  }
  .card--front .brand {
    position: absolute;
    left: 0; right: 0;
    top: 78px;
    justify-content: center;
  }
  .card--front .brand__name { font-size: 60px; }
  .card--front .brand__dot { width: 28px; height: 28px; }
</style>
</head>
<body>
<main class="sheet">
  <section class="card card--back" aria-label="Card back">
    <div class="brand">
      <span class="brand__dot"></span>
      <span class="brand__name">Bigotes, Inc</span>
    </div>
    <p class="contact__name">Lorenza Mireles</p>
    <p class="contact__phone">(555) 812-3762</p>
    <p class="contact__email">bigotesinc@correomail.net</p>
    <p class="tagline">A paw-bulous service is guaranteed!</p>
  </section>

  <section class="card card--front" aria-label="Card front">
    <svg class="card__wave" viewBox="0 0 540 310" preserveAspectRatio="none" aria-hidden="true">
      <path d="M0,178 C140,150 300,205 540,238 L540,310 L0,310 Z" fill="var(--card-blue)"/>
      <path d="M210,236 C350,244 470,215 540,140 L540,178 C470,240 360,260 210,236 Z" fill="var(--accent-orange)"/>
    </svg>
    <div class="brand">
      <span class="brand__dot"></span>
      <span class="brand__name">Bigotes, Inc</span>
    </div>
  </section>
</main>
</body>
</html>
```